Software Product Website Design

We have a software product which we have just renamed from Milestone Linked Tracking (MLT) to Brolvane. The web site is for www.brolvane-demo.com and needs to contain certain information related to our software product in accordance with the information contained in the previous product brochure (see attached). The logo file is also attached but the designer is free to propose alternative logo colours. The theme for the website must be based on the selected logo colours..
Target Market(s)
Project Management, Engineering, Construction etc companies involved with projects in all industries world-wide
Industry/Entity Type
Software
Coding
Coded - Design and coding required
Number of Pages Required
1 page
Font styles to use
Requirements
Must have
- Professional but exciting theme. The contents of the attached brochure should be included.

```html
<!DOCTYPE html>
<html lang="en">
<head>
<meta charset="utf-8">
<title>Brolvane — Milestone Linked Tracking Software</title>
<link href="https://fonts.googleapis.com/css2?family=Open+Sans:wght@300;400;600;700&display=swap" rel="stylesheet">
<style>
:root{
  --brand-blue:#1e88e5;
  --hero-top:#1a9bf0;
  --hero-bottom:#1b63c9;
  --accent-red:#e0183d;
  --ink:#3a3f47;
  --muted:#7d848d;
  --light-bg:#f1f2f4;
  --band-blue:#2a8fe8;
  --navy:#0d1b3a;
  --navy-deep:#08132b;
  --line:#d9dce0;
  --white:#ffffff;
}
*{box-sizing:border-box;margin:0;padding:0}
html,body{width:1200px;height:2588px;overflow:hidden}
body{font-family:"Open Sans",Arial,sans-serif;color:var(--ink);background:var(--white)}
.page{position:relative;width:1200px;height:2588px}
section,header,footer{position:relative;width:1200px}
.wrap{position:relative;width:960px;margin:0 auto;height:100%}

/* header */
.site-header{height:56px;background:var(--white)}
.brand{position:absolute;left:0;top:12px;display:flex;align-items:center;gap:10px}
.brand-mark{width:30px;height:30px;background:var(--brand-blue);border-radius:4px}
.brand-name{font-size:24px;font-weight:700;color:var(--ink);letter-spacing:-.3px}
.main-nav{position:absolute;right:0;top:20px;display:flex;gap:30px}
.main-nav a{font-size:12px;font-weight:600;color:var(--ink);text-decoration:none;letter-spacing:.5px}

/* hero */
.hero{height:290px;background:linear-gradient(180deg,var(--hero-top),var(--hero-bottom))}
.hero-copy{position:absolute;left:0;top:62px;width:440px;color:var(--white)}
.hero-copy h1{font-size:30px;font-weight:700;line-height:1.2}
.hero-copy h2{font-size:18px;font-weight:400;margin-top:4px}
.hero-copy p{font-size:11px;line-height:1.55;margin-top:14px;opacity:.9}
.btn{display:inline-block;background:var(--accent-red);color:var(--white);font-size:12px;font-weight:600;padding:9px 18px;border-radius:3px;text-decoration:none}
.hero-copy .btn{margin-top:16px}
.slider-dots{display:flex;gap:6px;margin-top:18px}
.slider-dots span{width:9px;height:9px;border-radius:50%;background:rgba(255,255,255,.5)}
.slider-dots span:first-child{background:var(--white)}
.hero-visual{position:absolute;right:30px;top:18px;width:400px;height:255px;border-radius:8px;background:linear-gradient(160deg,#f4f6f8,#c9d3dc)}

/* partner strip */
.partners{height:100px;background:var(--light-bg)}
.partner-row{position:absolute;left:0;right:0;top:36px;display:flex;justify-content:space-between}
.partner-row span{font-size:20px;font-weight:700;color:#8b9096;letter-spacing:1px}

/* about */
.about{height:300px;text-align:center}
.section-title{font-size:32px;font-weight:400;color:var(--ink)}
.about .section-title{padding-top:46px}
.about p{font-size:11px;line-height:1.7;color:var(--muted);margin:14px auto 0;width:900px}

/* process */
.process{height:490px;background:var(--light-bg)}
.process .section-title{position:absolute;top:34px;left:0;right:0;text-align:center;font-size:24px}
.process-lines{position:absolute;left:0;top:0}
.process-screen{position:absolute;left:300px;top:92px;width:380px;height:250px;border:6px solid #2b2f35;border-radius:6px;background:linear-gradient(160deg,#fafbfc,#d5dde4)}
.step{position:absolute;width:190px;text-align:center}
.step svg{display:block;margin:0 auto 4px}
.step h3{font-size:12px;font-weight:700;letter-spacing:.5px;color:var(--hero-bottom)}
.step p{font-size:10px;line-height:1.5;color:var(--muted);margin-top:3px}

/* feature rows */
.feature{height:270px}
.feature.alt{height:330px;background:#f6f7f8}
.feature-text{position:absolute;top:54px;width:440px}
.feature-text h2{font-size:28px;font-weight:400}
.feature-text p{font-size:11px;line-height:1.65;color:var(--muted);margin-top:12px}
.feature-text .btn{margin-top:14px}
.feature-img{position:absolute;border-radius:4px}

/* newsletter */
.newsletter{height:250px;margin-top:40px;background:var(--band-blue);text-align:center;color:var(--white)}
.newsletter h2{font-size:26px;font-weight:400;padding-top:56px}
.newsletter p{font-size:15px;margin-top:4px;opacity:.92}
.signup{display:flex;justify-content:center;margin-top:24px}
.signup .field{width:300px;height:36px;background:var(--white);border-radius:3px 0 0 3px;color:#9aa0a6;font-size:12px;text-align:left;padding:10px 14px}
.signup .submit{height:36px;padding:10px 22px;background:var(--navy);font-size:13px;font-weight:700;border-radius:0 3px 3px 0}

/* footer */
.site-footer{height:420px;background:var(--navy)}
.footer-cols{position:absolute;top:50px;left:0;right:0;display:flex;justify-content:space-between}
.footer-col{width:170px}
.footer-col h4{font-size:12px;font-weight:700;color:var(--white);letter-spacing:.5px;margin-bottom:12px}
.footer-col li{list-style:none;font-size:11px;line-height:1.75;color:#aab4c6}
.socials{display:flex;gap:8px;margin-top:12px}
.socials span{width:18px;height:18px;border-radius:50%;background:#aab4c6}
.legal{height:88px;background:var(--navy-deep)}
.legal p{position:absolute;left:0;top:34px;font-size:11px;color:#8f9ab0}
</style>
</head>
<body>
<div class="page">

<header class="site-header">
  <div class="wrap">
    <div class="brand"><span class="brand-mark"></span><span class="brand-name">Brolvane</span></div>
    <nav class="main-nav">
      <a href="#">ABOUT US</a><a href="#">SERVICES</a><a href="#">PRODUCT</a><a href="#">SUPPORT</a><a href="#">RESOURCES</a>
    </nav>
  </div>
</header>

<section class="hero">
  <div class="wrap">
    <div class="hero-copy">
      <h1>Proin nulla arcu nonummy</h1>
      <h2>Aliquam nec erat at purus cursus</h2>
      <p>In cursus lacus ac nisl rhoncus, vel blandit mi tempus. Sed porta augue id nulla dictum, at laoreet sem gravida. Integer vel dolor a felis lacinia tristique.</p>
      <a class="btn" href="#">Learn More</a>
      <div class="slider-dots"><span></span><span></span><span></span><span></span></div>
    </div>
    <div class="hero-visual" role="img" aria-label="Desktop monitor showing the Brolvane project tracking dashboard with Gantt chart"></div>
  </div>
</section>

<section class="partners">
  <div class="wrap">
    <div class="partner-row">
      <span>KESTREL</span><span>Halden</span><span>NORVIK</span><span>Tessaly</span><span>MALTROP</span><span>HALVER</span>
    </div>
  </div>
</section>

<section class="about">
  <div class="wrap">
    <h2 class="section-title">About Our Software Product</h2>
    <p>Brolvane links every deliverable on a project to its milestone, so teams see at a glance what is done, what is late and what it costs. Built for project managers, engineers and contractors, it brings schedule, budget and progress into one clear view that the whole team can trust from the first day.</p>
    <p>From the planning stage through to final handover, Brolvane keeps reports tied to real outputs rather than hours logged. Managers can measure earned value, spot slippage early and share status with clients in a format they understand. The result is fewer surprises, faster decisions and projects that finish on time and within budget across every industry.</p>
  </div>
</section>

<section class="process">
  <div class="wrap">
    <h2 class="section-title">Our Product Process</h2>
    <svg class="process-lines" width="960" height="490" aria-hidden="true">
      <g fill="none" stroke="#c6ccd3" stroke-width="1.5">
        <path d="M170 150 Q240 150 300 170"/>
        <path d="M170 270 Q240 270 300 250"/>
        <path d="M170 380 Q240 380 300 330"/>
        <path d="M800 150 Q740 150 680 170"/>
        <path d="M800 330 Q740 330 680 300"/>
      </g>
    </svg>
    <div class="process-screen" role="img" aria-label="Brolvane application screen with progress curves and task table"></div>

    <div class="step" style="left:-10px;top:110px">
      <svg width="30" height="30"><circle cx="15" cy="15" r="14" fill="#e0183d"/><circle cx="15" cy="15" r="5" fill="none" stroke="#fff" stroke-width="2"/></svg>
      <h3>CONTROL</h3><p>Set baselines and keep each milestone in check.</p>
    </div>
    <div class="step" style="left:-10px;top:232px">
      <svg width="30" height="30"><circle cx="15" cy="15" r="14" fill="#e0183d"/><path d="M8 19 L13 13 L17 17 L22 10" fill="none" stroke="#fff" stroke-width="2"/></svg>
      <h3>IMPROVE</h3><p>Act early on slippage and refine the plan.</p>
    </div>
    <div class="step" style="left:-10px;top:344px">
      <svg width="30" height="30"><circle cx="15" cy="15" r="14" fill="#e0183d"/><rect x="9" y="14" width="3" height="7" fill="#fff"/><rect x="14" y="10" width="3" height="11" fill="#fff"/><rect x="19" y="12" width="3" height="9" fill="#fff"/></svg>
      <h3>ANALYZE</h3><p>Compare planned and earned value per deliverable.</p>
    </div>
    <div class="step" style="left:780px;top:110px">
      <svg width="30" height="30"><circle cx="15" cy="15" r="14" fill="#e0183d"/><rect x="9" y="9" width="12" height="12" fill="none" stroke="#fff" stroke-width="2"/></svg>
      <h3>DEFINE</h3><p>Break scope into clear, measurable deliverables.</p>
    </div>
    <div class="step" style="left:780px;top:294px">
      <svg width="30" height="30"><circle cx="15" cy="15" r="14" fill="#e0183d"/><rect x="8" y="9" width="14" height="10" fill="none" stroke="#fff" stroke-width="2"/><path d="M12 22 H18" stroke="#fff" stroke-width="2"/></svg>
      <h3>MEASURE</h3><p>Track true progress against every milestone.</p>
    </div>
  </div>
</section>

<section class="feature">
  <div class="wrap">
    <div class="feature-text" style="left:0">
      <h2>Why Choose Our Product</h2>
      <p>Brolvane replaces scattered spreadsheets with one shared source of truth. Every task, cost and document is linked to the milestone it serves, so progress is measured by results.</p>
      <p>Set up takes days, not months. Teams get live dashboards, clear client reports and alerts before small delays become big ones, on any project size.</p>
      <a class="btn" href="#" style="background:var(--hero-bottom)">Learn More</a>
    </div>
    <div class="feature-img" role="img" aria-label="Laptop and printed charts on a desk" style="left:600px;top:44px;width:360px;height:200px;background:linear-gradient(150deg,#eef1f4,#b9c3cc)"></div>
  </div>
</section>

<section class="feature alt">
  <div class="wrap">
    <div class="feature-img" role="img" aria-label="Brolvane progress report screen on a laptop" style="left:0;top:60px;width:380px;height:200px;background:linear-gradient(150deg,#f3f5f7,#c1ccd6)"></div>
    <div class="feature-text" style="left:520px;top:70px">
      <h2>Progress &amp; Reports</h2>
      <p>Generate progress reports in one click. Show completion by deliverable, earned value curves and forecast dates in a layout clients read with ease.</p>
      <p>Export to PDF or share a live link. Every figure traces back to its source, so audits and reviews are quick and painless for your team.</p>
      <a class="btn" href="#">Learn More</a>
    </div>
  </div>
</section>

<section class="newsletter">
  <h2>Donec dictum lectus non odio ante vitae</h2>
  <p>Proin iaculis aliquam mauris nunc quam venenatis nec euismod sit amet egestas</p>
  <div class="signup"><div class="field">Email Address</div><div class="submit">SIGN UP</div></div>
</section>

<footer class="site-footer">
  <div class="wrap">
    <div class="footer-cols">
      <div class="footer-col"><h4>COMPANY</h4><ul><li>Why Choose Us</li><li>How It Works</li><li>Product</li><li>Overview</li><li>Management</li></ul></div>
      <div class="footer-col"><h4>SERVICES</h4><ul><li>Planning Aids</li><li>Setup</li><li>Training</li><li>Deliverable Reports</li><li>Licences</li></ul></div>
      <div class="footer-col"><h4>RESOURCES</h4><ul><li>Help &amp; Support</li><li>Blogs</li><li>Reviews</li><li>Clients</li></ul></div>
      <div class="footer-col"><h4>SUPPORT</h4><ul><li>Terms of Use</li><li>Privacy Policy</li><li>Support</li><li>FAQ</li></ul></div>
      <div class="footer-col" style="width:200px"><h4>CONTACT US</h4><ul><li>12 Sample Road, Suite 4</li><li>Phone: +00 0 5550 1234</li><li>hello@brolvane-demo.com</li><li>www.brolvane-demo.com</li></ul><div class="socials"><span></span><span></span><span></span><span></span></div></div>
    </div>
  </div>
</footer>
<div class="legal"><div class="wrap"><p>© 2024 Brolvane. All rights reserved. Terms of Use.</p></div></div>

</div>
</body>
</html>
```